Harborline Optical -Window Poster (Optometrist)

We are an optometry practice and we need a poster for a new store promotion for our window highlighting we now also sell 2 pairs of glasses as a package deal. The size will be 1300mm width x 1900mm height

The artwork will be displayed as a fabric banner in our shop window. We have 7 other banners with different services our business provides. The words needs to standout for passers by and the cars stopped at the traffic lights out front of our business. We already have signs with our logos phone number etc. so we won't need them included in the poster.

It would need to include the following information.

Two pair packages now available*

*Conditions apply
Updates

The artwork will be displayed as a fabric banner in our shop window. We have 7 other banners with different services our business provides. The words needs to standout for passers by and the cars stopped at the traffic lights out front of our business. We already have signs with our logos phone number etc. so we won't need them included in the poster. Thank you for your work it's amazing Added Saturday, February 18, 2017

The artwork will be displayed as a fabric banner in our shop window. We have 7 other banners with different services our business provides. The words needs to standout for passers by and the cars stopped at the traffic lights out front of our business. We already have signs with our logos phone number etc. so we won't need them included in the poster. Added Saturday, February 18, 2017

Target Market(s)

Cars driving past and stopped at traffic lights outside our store.

Industry/Entity Type

Optician

Requirements
Must have
• Poster must say:
• Two pair packages now available*
• *Conditions apply

```html
<!DOCTYPE html>
<html lang="en">
<head>
<meta charset="utf-8">
<title>Two Pair Packages – Window Poster</title>
<link href="https://fonts.googleapis.com/css2?family=Archivo+Black&family=Bungee+Inline&family=Oswald:wght@500&family=Overpass:wght@400&display=swap" rel="stylesheet">
<style>
  :root {
    --night: #050605;
    --moss: #2c3a1c;
    --teal: #1d3a33;
    --lime: #6d7a2c;
    --orange: #f5a01f;
    --gold: #c9a42a;
    --white: #ffffff;
    --ribbon: #e0201f;
    --ribbon-dark: #a8120f;
  }
  html, body {
    margin: 0;
    padding: 0;
    width: 962px;
    height: 1200px;
    overflow: hidden;
    background: var(--night);
  }
  .poster {
    position: relative;
    width: 962px;
    height: 1200px;
    overflow: hidden;
    background: var(--night);
  }
  .nebula {
    position: absolute;
    inset: 0;
    background:
      radial-gradient(ellipse 300px 260px at 760px 560px, rgba(109,122,44,0.55), transparent 70%),
      radial-gradient(ellipse 380px 300px at 500px 800px, rgba(29,58,51,0.75), transparent 72%),
      radial-gradient(ellipse 420px 220px at 300px 240px, rgba(44,58,28,0.6), transparent 70%),
      radial-gradient(ellipse 260px 200px at 860px 1080px, rgba(44,58,28,0.45), transparent 70%),
      radial-gradient(ellipse 200px 160px at 120px 1150px, rgba(44,58,28,0.5), transparent 70%),
      var(--night);
  }
  .flare {
    position: absolute;
    left: 0;
    top: 0;
    width: 962px;
    height: 1200px;
  }
  .headline-top {
    position: absolute;
    right: 25px;
    top: 80px;
    margin: 0;
    font-family: "Overpass", sans-serif;
    font-weight: 400;
    font-size: 80px;
    line-height: 1;
    letter-spacing: 1px;
    color: var(--orange);
  }
  .ribbon {
    position: absolute;
    left: 0;
    top: 321px;
    width: 962px;
    height: 76px;
  }
  .headline-main {
    position: absolute;
    left: 0;
    right: 0;
    top: 285px;
    margin: 0;
    text-align: center;
    font-family: "Archivo Black", sans-serif;
    font-size: 146px;
    line-height: 1;
    color: var(--white);
    text-shadow: 5px 5px 0 var(--ribbon);
    padding-left: 10px;
  }
  .headline-sub {
    position: absolute;
    left: 0;
    right: 0;
    top: 452px;
    margin: 0;
    text-align: center;
    font-family: "Bungee Inline", sans-serif;
    font-weight: 400;
    font-size: 80px;
    line-height: 1;
    letter-spacing: 3px;
    color: var(--orange);
  }
  .conditions {
    position: absolute;
    left: 0;
    right: 0;
    top: 1030px;
    margin: 0;
    text-align: center;
    font-family: "Oswald", sans-serif;
    font-weight: 500;
    font-size: 56px;
    line-height: 1;
    letter-spacing: 6px;
    color: var(--gold);
  }
  .conditions-rule {
    position: absolute;
    left: 345px;
    top: 1104px;
    width: 330px;
    height: 2px;
    background: linear-gradient(90deg, transparent, #e8e2c8 30%, #e8e2c8 70%, transparent);
  }
</style>
</head>
<body>
  <main class="poster">
    <div class="nebula" role="img" aria-label="Dark cosmic nebula texture in black, moss green and teal"></div>

    <svg class="flare" viewBox="0 0 962 1200" aria-hidden="true">
      <defs>
        <linearGradient id="streak" x1="0" x2="1">
          <stop offset="0" stop-color="#9fb7c4" stop-opacity="0"/>
          <stop offset="0.5" stop-color="#9fb7c4" stop-opacity="0.55"/>
          <stop offset="1" stop-color="#9fb7c4" stop-opacity="0"/>
        </linearGradient>
        <radialGradient id="glint">
          <stop offset="0" stop-color="#ffffff" stop-opacity="0.7"/>
          <stop offset="1" stop-color="#ffffff" stop-opacity="0"/>
        </radialGradient>
      </defs>
      <rect x="480" y="174" width="482" height="3" fill="url(#streak)"/>
      <rect x="0" y="175" width="260" height="2" fill="url(#streak)"/>
      <rect x="0" y="292" width="420" height="2" fill="url(#streak)"/>
      <circle cx="45" cy="172" r="32" fill="url(#glint)"/>
    </svg>

    <h2 class="headline-top">NOW AVAILABLE*</h2>

    <svg class="ribbon" viewBox="0 0 962 76" aria-hidden="true">
      <polygon points="0,0 100,0 84,38 100,76 0,76" fill="var(--ribbon)"/>
      <polygon points="862,0 962,0 962,76 862,76 878,38" fill="var(--ribbon)"/>
    </svg>

    <h1 class="headline-main">TWO PAIR</h1>
    <h2 class="headline-sub">PACKAGES</h2>

    <p class="conditions">*CONDITIONS APPLY</p>
    <div class="conditions-rule"></div>
  </main>
</body>
</html>
```